B2B EDM Banner Design- Specialist Tech Company

We need a new top-of-email banner for our EDM campaigns for Varnel Brix (www.varnelbrix-example.com
). This banner will sit at the top of every email and must immediately signal the brand, look modern and professional, and be visually aligned with the tech/IT audience.
Size of the banner: Around 728x90 - it must fit at the top of an email blast.
Purpose of the Banner
Establish a strong, recognizable brand identity across all Varnel Brix EDMs
visually consistent with existing banners created for other brands (see reference examples provided)
Communicate Varnel Brix’s value proposition at a glance
Brand Name
Varnel Brix
Tagline (must appear in the banner)
“11,322 whitepapers from 726 companies”
Design Requirements
Style & Tone
Modern, clean, and professional
Tech-centric look and feel
High-quality, sleek, and corporate
Eye-catching but not cluttered
Should feel premium and authoritative
Layout & Composition
Full-width banner for email header
Horizontal orientation similar to the Plomtar and Quindle Staff Archive examples
Include space for the brand name/logo prominently on the left or centered
Integrate the tagline in a readable, secondary position
Optional: a subtle background texture or tech-related abstract pattern (circuitry, network nodes, gradient, etc.)
No busy imagery—should feel clean and trustworthy
Color Palette
Use colors consistent with Varnel Brix branding from www.varnelbrix-example.com
Blues, greys, blacks, and tech-style gradients preferred
Should feel consistent with a B2B IT audience
Typography
Clean, sans-serif fonts (professional/tech-aligned)
Brand name should be bold and prominent
Tagline should be smaller, but still readable on desktop and mobile
Imagery (if used)
Abstract tech shapes, network visuals, geometric patterns, or gradient overlays
Avoid photography of people
Keep imagery subtle so text remains legible
Call-to-Action Button (optional)
None required in this banner (unlike the HR examples)
Banner should remain a pure brand header
Deliverables
Final banner in PNG and JPG formats
2–3 design variations (if possible) for A/B testing
Dimensions optimized for EDM: ~600–700px wide (standard email width), proportionate height

```html
<!DOCTYPE html>
<html lang="en">
<head>
<meta charset="utf-8">
<title>Varnel Brix – Email Header Banner</title>
<link href="https://fonts.googleapis.com/css2?family=Montserrat:wght@500;600;800&display=swap" rel="stylesheet">
<style>
  :root {
    --page-grey: #8a8a8a;
    --banner-black: #05070b;
    --brand-blue: #1a9be0;
    --deep-blue: #0b3fb8;
    --sky-blue: #7fd0f5;
    --white: #ffffff;
  }
  html, body {
    margin: 0;
    padding: 0;
    width: 1200px;
    height: 193px;
    overflow: hidden;
    background: var(--page-grey);
  }
  .banner {
    position: absolute;
    left: 240px;
    top: 51px;
    width: 722px;
    height: 91px;
    background: var(--banner-black);
    overflow: hidden;
    font-family: "Montserrat", Arial, sans-serif;
  }
  .banner__swoosh {
    position: absolute;
    left: 0;
    top: 0;
  }
  .banner__network {
    position: absolute;
    right: 0;
    top: 0;
    width: 260px;
    height: 91px;
    background:
      radial-gradient(ellipse 90px 50px at 65% 45%, rgba(120,200,255,0.55), transparent 70%),
      radial-gradient(ellipse 160px 80px at 70% 55%, rgba(20,90,170,0.55), transparent 75%),
      linear-gradient(90deg, var(--banner-black) 0%, #07142a 40%, #0b2446 100%);
  }
  .brand {
    position: absolute;
    left: 36px;
    top: 0;
    height: 91px;
    display: flex;
    align-items: center;
    gap: 10px;
  }
  .brand__mark {
    width: 36px;
    height: 36px;
    border-radius: 50%;
    background: var(--brand-blue);
  }
  .brand__name {
    color: var(--white);
    font-weight: 800;
    font-size: 27px;
    letter-spacing: -0.3px;
    text-transform: uppercase;
    line-height: 1;
  }
  .divider {
    position: absolute;
    left: 325px;
    top: 18px;
    width: 2px;
    height: 56px;
    background: var(--brand-blue);
  }
  .tagline {
    position: absolute;
    left: 344px;
    top: 27px;
    margin: 0;
    color: var(--white);
    font-weight: 500;
    font-size: 16px;
    line-height: 19px;
  }
  .tagline strong {
    color: var(--brand-blue);
    font-weight: 800;
  }
</style>
</head>
<body>
  <header class="banner">
    <svg class="banner__swoosh" width="320" height="91" viewBox="0 0 320 91" aria-hidden="true">
      <defs>
        <linearGradient id="swooshGradient" x1="0" y1="0" x2="1" y2="0.4">
          <stop offset="0" stop-color="var(--sky-blue)"/>
          <stop offset="0.35" stop-color="var(--brand-blue)"/>
          <stop offset="1" stop-color="var(--deep-blue)"/>
        </linearGradient>
      </defs>
      <path d="M0,0 L195,0 C235,28 270,60 300,91 L262,91 C205,50 120,22 0,14 Z" fill="url(#swooshGradient)"/>
    </svg>

    <div class="banner__network" role="img" aria-label="Abstract glowing blue network of connected nodes"></div>

    <div class="brand">
      <span class="brand__mark" aria-hidden="true"></span>
      <span class="brand__name">Varnel Brix</span>
    </div>

    <div class="divider" aria-hidden="true"></div>

    <p class="tagline"><strong>11,322</strong> Whitepapers<br>from <strong>726 Companies</strong></p>
  </header>
</body>
</html>
```